Logo Design - Wine Range

Hello Designers,
We need a graphic design for a new logo for a wine range that we are releasing in coming months and are wanting to design a logo that reflects the name in a unique and creative way.
The Name is HERON GLEN.
We are really wanting the Logo/label to have a visual element which in a quick glance it is visually symbolic and one to remember.
Brief
A )Label with be 10 cm length and 9cm width, wanting picture to be about 5cm in Length. Information on the front label needs to be Name - Heron Glen
B) Looking for BRIGHT AND BOLD colours that attract and relate to Australian Nature. Can also include Falcon Bird but not necessary.
The designer who is selected as winner will need to create a label in order to complete the project. Goodluck :)
Thank you for your interest, looking forward to reviewing designs soon.
Updates
Label with be 10 cm length and 9cm width, wanting picture to be about 5cm in Length. Information on the front label needs to be Name - Heron Glen
have attached a colour palette of Australian Nature for an idea of colour.
Target Market(s)
Age group 18+
Industry/Entity Type
Graphic Design
Requirements
Must have
- Must include a graphic design not just words
Nice to have
- Unique and modern touch, If using Falcon would like the bird to be whole, Australian Nature. Rocks, waterfalls... the sky is the limit really , goodluck

```html
<!DOCTYPE html>
<html lang="en">
<head>
<meta charset="utf-8">
<title>Heron Glen – Wine Labels</title>
<link rel="stylesheet" href="https://fonts.googleapis.com/css2?family=Cinzel:wght@400&family=Tenor+Sans&display=swap">
<style>
  :root {
    --backdrop: #cbcbcb;
    --shiraz: #7d3a1f;
    --shiraz-edge: #5e2812;
    --paper: #ffffff;
    --paper-edge: #e4e4e4;
    --gold: #f39a1c;
    --sky: #1f7fb0;
    --sky-light: #e6f2f8;
    --ink-dark: #2a2a2a;
    --ink-light: #f5efe8;
  }
  * { margin: 0; padding: 0; box-sizing: border-box; }
  html, body {
    width: 1200px; height: 900px; overflow: hidden;
    background: var(--backdrop);
  }
  .canvas {
    width: 1200px; height: 900px;
    display: flex; align-items: center; justify-content: center; gap: 90px;
  }
  .label {
    position: relative;
    width: 276px; height: 306px;
    box-shadow: 0 1px 3px rgba(0,0,0,0.25);
    display: flex; flex-direction: column; align-items: center;
  }
  .label--shiraz {
    background: linear-gradient(90deg, var(--shiraz-edge) 0%, var(--shiraz) 25%, var(--shiraz) 75%, var(--shiraz-edge) 100%);
    color: var(--ink-light);
  }
  .label--merlot {
    background: linear-gradient(90deg, var(--paper-edge) 0%, var(--paper) 22%, var(--paper) 78%, var(--paper-edge) 100%);
    color: var(--ink-dark);
  }
  .rule-pair {
    position: absolute; left: 13px; right: 13px; height: 6px;
    border-top: 1.5px solid var(--gold);
    border-bottom: 1.5px solid var(--gold);
  }
  .rule-pair--top { top: 7px; }
  .rule-pair--bottom { bottom: 9px; }
  .vintage {
    margin-top: 26px;
    font-family: "Cinzel", serif;
    font-size: 12px; letter-spacing: 2px;
  }
  .brand-mark {
    margin-top: 30px;
    width: 66px; height: 66px;
    background: linear-gradient(180deg, var(--sky) 0%, var(--sky) 45%, var(--sky-light) 100%);
  }
  .brand-name {
    margin-top: 20px;
    font-family: "Tenor Sans", sans-serif;
    font-weight: 400;
    color: var(--gold);
    text-align: center; line-height: 1;
  }
  .brand-name__first { display: block; font-size: 17px; letter-spacing: 2px; }
  .brand-name__second { display: block; font-size: 30px; letter-spacing: 1px; margin-top: 3px; }
  .region {
    position: absolute; bottom: 30px; left: 0; right: 0;
    text-align: center;
    font-family: "Cinzel", serif;
    font-size: 11px; letter-spacing: 2.6px;
  }
</style>
</head>
<body>
  <main class="canvas">
    <section class="label label--shiraz">
      <div class="rule-pair rule-pair--top"></div>
      <p class="vintage">SHIRAZ 2012</p>
      <div class="brand-mark" role="img" aria-label="Heron Glen brand mark"></div>
      <h1 class="brand-name"><span class="brand-name__first">HERON</span><span class="brand-name__second">GLEN</span></h1>
      <p class="region">SOUTH AUSTRALIA</p>
      <div class="rule-pair rule-pair--bottom"></div>
    </section>

    <section class="label label--merlot">
      <div class="rule-pair rule-pair--top"></div>
      <p class="vintage">MERLOT 2012</p>
      <div class="brand-mark" role="img" aria-label="Heron Glen brand mark"></div>
      <h2 class="brand-name"><span class="brand-name__first">HERON</span><span class="brand-name__second">GLEN</span></h2>
      <p class="region">SOUTH AUSTRALIA</p>
      <div class="rule-pair rule-pair--bottom"></div>
    </section>
  </main>
</body>
</html>
```